Poster for a Bicycle show/Expo

We need a poster for a Bicycle show/Expo and sustainable transport. Exhibitors will sell bikes, cycling clothing, accessories, etc. ...
This show is annual and the Poster is for the 2015 edition.

The style must be modern, dynamic, bright colors.

Your concept must be compatible in a landscape format. (We will ourselves adaptations of different formats.)
Width: 210 mm
Height: 297 mm
It's necessary for us to have the source file (vector) for make, later, the different format (flyers, website, ...)

Content of the Poster:
- 1 big picture (no clip art)
- Big title: « Fête Roulix » (« Salon » or « Salon du » can be small and « Vélo » big.)
- Subtitle: « et de la mobilité douce »
- Date: « 8, 9 et 10 mai 2015 » or « 8-10 mai 2015 »
- Place: « Halle TRX - Quai Brenaz »
- Text line 1: « www.fete-roulix.ch - Entrée gratuite »
- Text line 2« Piste d’essais - Restauration sur place »
- Text line 3: « Ve 8 mai de 17h à 21h - Sa 9 mai de 10h à 20h - Di 10 mai de 10h à 18h »
- Please, leave a zone in the poster for sponsors logos
(The predominant information (most visible) are: « Fête Roulix » and « 8, 9 et 10 mai 2015 or 8-10 mai 2015 »)

Content of the big picture:
- from a cheap stock, like PixoBanq.com
- a bicycle in action or a detail of a bicycle (or a accessory) (no race bike)
- a modern picture with bright colors.
- if a person is on the picture, we prefer a men
- not an aerial view with cyclists in a landscape.

Some examples of poster of shows - with typo-title worked

http://www.bassinexpoville.com/Temp/IMG/F_a7c2e9b4d1f0836255e1b7a9c4d3f2e6812c9b0a4e5f7_200_296.png

http://qz4m.tolvanfoires.fr/Data/kmtolv_mer/block/F_9bd1c3e7f2a4605813c9e2d7b4a8f6c0d3e1a527f86c2.pdf
(page 2 of this PDF)

http://salons.marvelle-agenda.fr/images/marvelle-agenda/foires-salons/phototheque/expo-moto-brivanne/expo-moto-brivanne2012-affiche.jpg

http://www.drupaix.net/blog/wp-content/uploads/2007/03/affiche-foire-des-pages.jpg

http://www.voilemarine-club.com/wp-content/affiche-regate-2007.jpg

Hello,

For information, for your next versions, please, add the text "Piste d'essais".

- Text line 1: « www.fete-roulix.ch - Entrée gratuite »
- Text line 2: « Piste d’essais - Restauration sur place »
- Text line 3: « Ve 8 mai de 17h à 21h - Sa 9 mai de 10h à 20h - Di 10 mai de 10h à 18h »

Thanks,
Mathieu

Landscape

Sans Serif

```html
<!DOCTYPE html>
<html lang="fr">
<head>
<meta charset="utf-8">
<title>Fête Roulix et de la mobilité douce — 8-10 mai 2015</title>
<link rel="stylesheet" href="https://fonts.googleapis.com/css2?family=Bebas+Neue&display=swap">
<style>
  :root {
    --ink-white: #ffffff;
    --bike-green: #5ee03a;
    --panel-dark: rgba(20, 24, 20, 0.82);
    --panel-green: rgba(78, 214, 52, 0.78);
    --panel-light: rgba(255, 255, 255, 0.5);
    --photo-grey: #7c7a72;
    --photo-earth: #5a5247;
    --photo-green: #3fae2a;
  }
  * { margin: 0; padding: 0; box-sizing: border-box; }
  html, body { width: 848px; height: 1200px; overflow: hidden; background: #fff; }
  .poster {
    position: relative;
    width: 848px;
    height: 1200px;
    overflow: hidden;
    font-family: "Bebas Neue", "Oswald", sans-serif;
    color: var(--ink-white);
  }
  .hero-photo {
    position: absolute;
    inset: 0;
    background:
      linear-gradient(160deg, transparent 30%, rgba(63,174,42,0.55) 42%, transparent 52%),
      radial-gradient(circle at 72% 40%, #9a9890 0%, transparent 35%),
      linear-gradient(200deg, var(--photo-grey) 0%, var(--photo-earth) 55%, #8b8578 100%);
  }
  .panel { position: absolute; }
  .title-panel {
    left: 43px; top: 40px; width: 449px; height: 437px;
    background: var(--panel-dark);
    text-align: center;
    padding-top: 42px;
  }
  .title-lead { font-size: 62px; line-height: 1; letter-spacing: 1px; }
  .title-main {
    font-size: 190px; line-height: 0.86; color: var(--bike-green);
    margin-top: 12px;
  }
  .subtitle { font-size: 23px; line-height: 1; margin-top: 22px; letter-spacing: 0.5px; }

  .info-panel {
    left: 43px; top: 520px; width: 449px; height: 637px;
    background: var(--panel-green);
    text-align: center;
    padding-top: 170px;
  }
  .event-date { font-size: 58px; line-height: 1; }
  .event-venue { font-size: 68px; line-height: 0.95; }
  .event-place { font-size: 40px; line-height: 1; }
  .event-details { list-style: none; margin-top: 44px; }
  .event-details li { font-size: 24px; line-height: 24px; letter-spacing: 0.3px; }

  .sponsor-zone {
    left: 534px; top: 712px; width: 271px; height: 445px;
    background: var(--panel-light);
  }
</style>
</head>
<body>
<div class="poster">
  <div class="hero-photo" role="img" aria-label="Photo en gros plan d'un vélo vert : cadre, patte arrière, moyeu, rayons et chaîne sur un sol de gravier"></div>

  <header class="panel title-panel">
    <p class="title-lead">FÊTE</p>
    <h1 class="title-main">ROULIX</h1>
    <p class="subtitle">ET DE LA MOBILITÉ DOUCE</p>
  </header>

  <section class="panel info-panel">
    <p class="event-date">8-10 MAI 2015</p>
    <p class="event-venue">HALLE TRX</p>
    <p class="event-place">QUAI BRENAZ</p>
    <ul class="event-details">
      <li>WWW.FETE-ROULIX.CH</li>
      <li>ENTRÉE GRATUITE</li>
      <li>PISTE D’ESSAIS</li>
      <li>RESTAURATION SUR PLACE</li>
      <li>VE 8 MAI DE 17H À 21H</li>
      <li>SA 9 MAI DE 10H À 20H</li>
      <li>DI 10 MAI DE 10H À 18H</li>
    </ul>
  </section>

  <aside class="panel sponsor-zone" aria-label="Zone réservée aux logos des partenaires"></aside>
</div>
</body>
</html>
```